Watercolour Order of the Day Wedding card

I am needing a card with the same feel (but not a copy) of the wildlife "invitation" template attached. This is an African wedding taking place in the wild.

The Front showing map-type layout with order of the day and back will be for a reading and also have water colour elements.

I would like both back and front to have a border and a watercolour, hand-painted feel. The back to please have a baobab.

Size A5 portrait OR horizontal

I have attached a series of artwork to help.

NO text to be added to back please, only front.

colourful palette is great!
Updates

Good evening, I will be extending my deadline until Midnight Tuesday 19th August as I have been delayed in resounding to designers. I look forward to the submissions and hugely thank all those that have been submitted so far. thank you

Font styles to use
Script

Colors
0054AA
0677BA
7BADD7
CADEEF
E8F1F8
0094D4
00A9DD
6FCCEA
C7EBF8
E9F6FB
00AB8E
00BBA5
67D7C9
C6EFE9
E9F9F6
FFF300
FFF600
FEFA6F
FFFEC7
FFFEE8
F0912C
F2A743
F7CA91
FBE8D2
FDF5EE
E54698
E96AAD
F1A4CE
F9D9EA
FCEFF6

Requirements
Must have
• Africa illustrations incorporated like Invitation

```html
<!DOCTYPE html>
<html lang="en">
<head>
<meta charset="utf-8">
<title>Order of the Day – Safari Wedding Cards</title>
<link rel="stylesheet" href="https://fonts.googleapis.com/css2?family=Alegreya:ital,wght@1,700&family=Dancing+Script:wght@700&display=swap">
<style>
  :root {
    --bg: #b8e8a8;
    --frame-green: #2f9a2a;
    --frame-lime: #b7d81f;
    --frame-yellow: #e6ec2a;
    --paper: #f7f6f2;
    --ink-brown: #7a3f12;
    --title-orange: #c0561d;
    --route-red: #b3322a;
    --sky: #8fc3e6;
    --sand: #d9cba4;
    --cloud: #dfe6ee;
    --ribbon: #8ea6bf;
    --foliage: #6f8f4c;
    --bark: #a7653b;
  }
  * { box-sizing: border-box; margin: 0; padding: 0; }
  html, body { width: 1200px; height: 795px; overflow: hidden; }
  body { background: var(--bg); position: relative; }

  .card {
    position: absolute;
    top: 97px;
    width: 427px;
    height: 600px;
    padding: 23px;
    background: var(--frame-green);
    border: 4px solid var(--frame-green);
    box-shadow: 0 6px 18px rgba(40, 80, 30, 0.25);
  }
  .card::before {
    content: "";
    position: absolute;
    inset: 3px;
    border: 14px solid var(--frame-lime);
    outline: 3px solid var(--frame-yellow);
    outline-offset: -9px;
  }
  .card--back { left: 143px; }
  .card--front { left: 630px; }

  .card__panel {
    position: relative;
    width: 100%;
    height: 100%;
    overflow: hidden;
  }

  .art {
    position: absolute;
    border-radius: 8px;
    z-index: 1;
  }

  /* Back card */
  .card--back .card__panel {
    background: linear-gradient(180deg, #d6e8f3 0%, var(--sky) 20%, #bcd6e6 40%, #e6e1d2 58%, var(--sand) 100%);
  }
  .art--leaves-left   { left: 0;   top: 0;   width: 100px; height: 46px;  background: linear-gradient(135deg, #4f7a55, #8fb08a); }
  .art--leaves-top    { left: 123px; top: 0; width: 122px; height: 58px;  background: linear-gradient(180deg, #3f6a5a, #7fa39a); }
  .art--bee-eater     { left: 262px; top: 0; width: 95px;  height: 62px;  background: linear-gradient(135deg, #8a6a4a, #5f9a8a); }
  .art--rhino         { left: 0;   top: 54px;  width: 112px; height: 72px;  background: linear-gradient(135deg, #8d918f, #b9bcb8); }
  .art--leopard       { left: 0;   top: 134px; width: 73px;  height: 126px; background: linear-gradient(180deg, #c79a5a, #8a6a3a); }
  .art--elephant      { left: 0;   top: 290px; width: 110px; height: 132px; background: linear-gradient(180deg, #a5a7a5, #7f8280); }
  .art--crane         { left: 0;   top: 432px; width: 92px;  height: 114px; background: linear-gradient(180deg, #6e6a72, #5f7f4a); }
  .art--lion          { left: 124px; top: 462px; width: 136px; height: 76px; background: linear-gradient(180deg, #c9a46e, #9b7a4a); }
  .art--zebra         { left: 292px; top: 76px;  width: 81px;  height: 86px;  background: linear-gradient(135deg, #e8e8e6, #6e6e6e); }
  .art--camera        { left: 316px; top: 168px; width: 57px;  height: 44px;  background: linear-gradient(180deg, #a8a48c, #7a7a64); }
  .art--jeep          { left: 259px; top: 220px; width: 114px; height: 84px;  background: linear-gradient(180deg, #8f9a5a, #5f6a44); }
  .art--baobab        { left: 251px; top: 312px; width: 122px; height: 234px; background: linear-gradient(180deg, #5f8a45 0%, #9b6a46 35%, var(--bark) 100%); }

  /* Front card */
  .card--front .card__panel { background: var(--paper); }
  .art--clouds { left: 8px; top: 46px; width: 357px; height: 72px; border-radius: 40px;
    background: linear-gradient(180deg, #eef2f6, var(--cloud) 60%, #e6dfee); }
  .art--ribbon { left: 85px; top: 25px; width: 238px; height: 44px; border-radius: 6px;
    background: linear-gradient(180deg, #a7bbcf, var(--ribbon)); }
  .art--bird-left { left: 0; top: 0; width: 56px; height: 52px;
    background: linear-gradient(135deg, #8b7fc4, #6fa7c9); }
  .art--bird-right { left: 306px; top: 6px; width: 67px; height: 52px;
    background: linear-gradient(135deg, #8e6a4a, #6e9a9a); }
  .art--sunrise { left: 27px; top: 81px; width: 81px; height: 50px;
    background: linear-gradient(90deg, #f5d36a, #d99a54); }
  .art--breakfast { left: 158px; top: 100px; width: 96px; height: 54px;
    background: linear-gradient(90deg, #c9d8a0, #8f7a45 60%, #b4582c); }
  .art--burger { left: 285px; top: 77px; width: 73px; height: 54px;
    background: linear-gradient(180deg, #e3a24a, #9a4e23); }
  .art--siesta { left: 236px; top: 204px; width: 77px; height: 62px;
    background: linear-gradient(180deg, #d9c38c, #a9a9a3); }
  .art--cocktail { left: 62px; top: 208px; width: 92px; height: 62px;
    background: linear-gradient(90deg, #c8b8a8, #6a4a34 60%, #e0a43a); }
  .art--supper { left: 35px; top: 339px; width: 104px; height: 58px;
    background: linear-gradient(90deg, #c99a5a, #b8c6dc 40%, #9aa6c2); }
  .art--finale { left: 223px; top: 320px; width: 70px; height: 73px;
    background: linear-gradient(180deg, #7c8ac9, #c77c6c 60%, #8a6a4a); }
  .art--dancers { left: 143px; top: 420px; width: 77px; height: 85px;
    background: linear-gradient(180deg, #f3c96a, #d4533e 55%, #4f8ab0); }
  .art--sign-after { left: 278px; top: 424px; width: 65px; height: 81px;
    background: linear-gradient(180deg, #e6d3a4, #b79a66 70%, #6e8a4a); }
  .art--tree-left { left: 0; top: 430px; width: 92px; height: 116px; border-radius: 46px 46px 0 0;
    background: linear-gradient(180deg, #c98a3e, #8a7a3a 60%, var(--foliage)); }
  .art--tree-right { left: 340px; top: 458px; width: 33px; height: 88px; border-radius: 16px 16px 0 0;
    background: linear-gradient(180deg, #2f4a3a, #3f5f4a); }
  .ground { position: absolute; left: 0; right: 0; bottom: 0; height: 40px; z-index: 0;
    background: linear-gradient(0deg, #dcd9cf, rgba(220,217,207,0)); }

  .title {
    position: absolute; left: 85px; top: 31px; width: 238px;
    text-align: center;
    font-family: "Dancing Script", cursive;
    font-weight: 700;
    font-size: 19px;
    color: var(--title-orange);
    transform: rotate(3deg);
    z-index: 2;
  }

  .route { position: absolute; inset: 0; width: 100%; height: 100%; z-index: 1; }
  .route path { fill: none; stroke: var(--route-red); stroke-width: 1.3; stroke-dasharray: 1.5 2.5; stroke-linecap: round; }

  .event {
    position: absolute;
    transform: translateX(-50%);
    text-align: center;
    font-family: "Alegreya", serif;
    font-style: italic;
    font-weight: 700;
    font-size: 11px;
    line-height: 1.3;
    color: var(--ink-brown);
    white-space: nowrap;
    z-index: 3;
  }
  .event__time { display: block; }

  .sign-text {
    position: absolute;
    transform: translateX(-50%);
    text-align: center;
    font-family: "Alegreya", serif;
    font-style: italic;
    font-weight: 700;
    font-size: 5px;
    line-height: 1.25;
    color: #3b2a18;
    white-space: nowrap;
    z-index: 3;
  }
</style>
</head>
<body>

<section class="card card--back">
  <div class="card__panel" role="img" aria-label="Watercolour sky fading into a sandy plain, framed by African wildlife">
    <div class="art art--leaves-left" role="img" aria-label="Watercolour tropical leaves"></div>
    <div class="art art--leaves-top" role="img" aria-label="Watercolour palm and fern leaves"></div>
    <div class="art art--bee-eater" role="img" aria-label="Watercolour bee-eater bird in flight"></div>
    <div class="art art--rhino" role="img" aria-label="Watercolour rhino among leaves"></div>
    <div class="art art--leopard" role="img" aria-label="Watercolour leopard climbing down"></div>
    <div class="art art--elephant" role="img" aria-label="Watercolour elephant"></div>
    <div class="art art--crane" role="img" aria-label="Watercolour crowned crane among ferns"></div>
    <div class="art art--lion" role="img" aria-label="Watercolour lion lying on a rock"></div>
    <div class="art art--zebra" role="img" aria-label="Watercolour zebra"></div>
    <div class="art art--camera" role="img" aria-label="Watercolour vintage camera"></div>
    <div class="art art--jeep" role="img" aria-label="Watercolour safari jeep"></div>
    <div class="art art--baobab" role="img" aria-label="Watercolour baobab tree with monkey, small bird and giraffe"></div>
  </div>
</section>

<section class="card card--front">
  <div class="card__panel">
    <div class="ground" aria-hidden="true"></div>
    <div class="art art--clouds" role="img" aria-label="Watercolour clouds"></div>
    <div class="art art--ribbon" role="img" aria-label="Watercolour blue ribbon banner"></div>
    <div class="art art--bird-left" role="img" aria-label="Watercolour hummingbird"></div>
    <div class="art art--bird-right" role="img" aria-label="Watercolour bee-eater bird in flight"></div>
    <h1 class="title">The Order of Things</h1>

    <svg class="route" viewBox="0 0 373 546" aria-hidden="true">
      <path d="M105 136 Q130 128 150 145"/>
      <path d="M252 132 Q265 126 280 130"/>
      <path d="M320 158 Q312 180 288 198"/>
      <path d="M232 240 Q190 230 152 270"/>
      <path d="M52 272 Q30 310 40 352"/>
      <path d="M150 360 Q185 335 218 370"/>
      <path d="M200 396 Q195 412 172 425"/>
      <path d="M223 476 Q250 455 276 478"/>
    </svg>

    <div class="art art--sunrise" role="img" aria-label="Smiling watercolour sun with two gold wedding rings"></div>
    <p class="event" style="left:68px; top:131px;"><span class="event__time">6.00 am</span>Sunrice Ceremony</p>

    <div class="art art--breakfast" role="img" aria-label="Champagne bottle, glasses and a breakfast spread on a table"></div>
    <p class="event" style="left:200px; top:156px;"><span class="event__time">7.00 am</span>Bush Breakfast</p>

    <div class="art art--burger" role="img" aria-label="Burger with sauce on a wooden board"></div>
    <p class="event" style="left:322px; top:134px;"><span class="event__time">10.00 am</span>Burger Break</p>

    <div class="art art--siesta" role="img" aria-label="Wooden signpost above a sleeping leopard"></div>
    <p class="sign-text" style="left:262px; top:214px;">Mopane Flats<br>Rhino Gate<br>Marula Camp</p>
    <p class="event" style="left:281px; top:269px;"><span class="event__time">Noon</span>Sensational Siesta</p>

    <div class="art art--cocktail" role="img" aria-label="Goat waiter and saxophone player"></div>
    <p class="event" style="left:102px; top:273px;"><span class="event__time">4.00 pm</span>Cocktail hour under the<br>tree of forgetfullness</p>

    <div class="art art--supper" role="img" aria-label="Wine bottle and a dressed banquet table"></div>
    <p class="event" style="left:89px; top:398px;"><span class="event__time">6.00 pm</span>Safari Supper</p>

    <div class="art art--finale" role="img" aria-label="Couple seated on a bench under an evening sky"></div>
    <p class="event" style="left:258px; top:400px;">Flaming Finale</p>

    <div class="art art--dancers" role="img" aria-label="Couple dancing under string lights"></div>
    <p class="event" style="left:181px; top:508px;">Into the night<br>Riverbed Razzle</p>

    <div class="art art--sign-after" role="img" aria-label="Wooden signpost"></div>
    <p class="sign-text" style="left:310px; top:436px;">Sable River<br>Airship<br>Kestrel Bridge</p>
    <p class="event" style="left:310px; top:508px;">After Party</p>

    <div class="art art--tree-left" role="img" aria-label="Watercolour autumn-coloured tree"></div>
    <div class="art art--tree-right" role="img" aria-label="Watercolour dark green tree"></div>
  </div>
</section>

</body>
</html>
```